Web Design Project for Communications Agency

The design I need (PSD file) is for an agency offering specialised PR and communications services for customers in the healthcare sector.

OBJECTIVES OF THE WEBSITE:
1. To promote the agency's communication services
2. To position Solène Verbruggen as an industry leader, an expert in healthcare PR and communications by highlighting blogposts and social media.

WHAT I NEED:
1st, I need the design for the Home Page ONLY.
Once approved, I will need the other pages designed as well. (Here is prototype that we've already developed for the Website that will guide you in the design:
http://qoravenlab.com/solenverbruggen/)

VISUAL INSPIRATION
We want to give this Website a "Flat Design" look. Here are some websites for inspiration :
- http://lumbrafolk.com/#!/process
- http://www.quillmarsh.co/
- http://dorvellink.com/

Also, reuse images found on the company's current Website :
http://www.solenverbruggen.com/fr/index.html

HOMEPAGE MAIN ELEMENTS:
1. Main menu : 6 sections
Accueil | Agence | Services | Approche | Publications | Contact

2. Main Call To Action (big dark rectangle in prototype):
Can be slider or just an information bloc.

3. Publications récentes :
The 4 latest blog posts must be features on the homepage (will be linked with the "Publications" section)

4. Dynamic Footer :
Contains a Chirpline feed and a Subscribe to our Newsletter feature (revecez nos publications)

OTHER PAGES (to design once Homepage is approved)
- Agence (about us)
- Services (our team)
- Approche (our approach)
- Publications (blog articles)
- Contact (Contact us)

• Please refer to prototype :
http://qoravenlab.com/solenverbruggen/
Must have ALL features present in prototype.

Also, must reuse this picture in the design : http://solenverbruggen.com/static/images/home-big-box.jpg

Finally, you will find attached the company logo.

```html
<!DOCTYPE html>
<html lang="fr">
<head>
<meta charset="utf-8">
<title>Solène Verbruggen — Gestion d'enjeux, affaires publiques</title>
<link rel="stylesheet" href="https://fonts.googleapis.com/css2?family=Oswald:wght@400;500&family=Open+Sans:ital,wght@0,400;0,600;1,400&display=swap">
<style>
:root{
  --red:#b3362f;
  --red-dark:#9a2b25;
  --red-deep:#8f2722;
  --red-input:#a32d27;
  --ink:#333;
  --muted:#666;
  --white:#fff;
  --grey-hero-1:#f3f3f3;
  --grey-hero-2:#cfcfcf;
}
*{box-sizing:border-box;margin:0;padding:0}
html,body{width:750px;height:1200px;overflow:hidden;background:var(--white)}
body{position:relative;font-family:"Open Sans",Arial,sans-serif;color:var(--ink)}
.abs{position:absolute}

/* header */
.site-header{position:absolute;left:0;top:0;width:750px;height:85px}
.nav-band{position:absolute;left:0;top:59px;width:750px;height:26px;background:var(--red)}
.brand{position:absolute;left:112px;top:0;width:94px;height:85px;background:var(--white);padding:10px 0 0 12px}
.brand-name{font-family:"Oswald",sans-serif;font-weight:400;color:var(--red);font-size:17px;line-height:17px;display:block}
.brand-tag{font-family:"Oswald",sans-serif;font-size:6.5px;line-height:8px;color:#555;margin-top:6px;display:block;border-top:1px solid #999;padding-top:3px;width:60px}
.main-nav{position:absolute;left:206px;top:59px;height:26px;display:flex}
.main-nav a{display:block;height:26px;line-height:26px;font-size:6.5px;font-weight:600;color:var(--white);text-decoration:none;text-align:center}
.main-nav a.active{background:var(--red-dark)}
.social{position:absolute;left:460px;top:22px;display:flex;gap:4px}
.social span{width:18px;height:18px;border-radius:3px;background:#4e9bbd}
.social span:nth-child(2){background:#2f6ea5}
.social span:nth-child(3){background:#8a8a99}
.lang-label{position:absolute;left:533px;top:27px;font-size:5.5px;color:#888}
.lang-select{position:absolute;left:584px;top:24px;width:53px;height:14px;border:1px solid #ccc;border-radius:2px;font-size:5.5px;line-height:12px;padding-left:5px;color:#444;display:flex;align-items:center;gap:3px}
.lang-select i{width:8px;height:5px;background:#6a7fb0;display:inline-block}

/* hero */
.hero{position:absolute;left:0;top:85px;width:750px;height:240px;background:radial-gradient(ellipse at 58% 45%,var(--grey-hero-1) 0%,#e2e2e2 55%,var(--grey-hero-2) 100%)}
.hero-title{position:absolute;left:112px;top:60px;font-family:"Oswald",sans-serif;font-weight:400;font-size:16px;line-height:20px;color:#3a3a3a;letter-spacing:.1px}
.hero-cta{position:absolute;left:112px;top:135px;width:179px;height:37px;background:var(--red);border-radius:2px;color:var(--white);font-family:"Oswald",sans-serif;font-size:16px;line-height:37px;text-align:center;box-shadow:0 1px 2px rgba(0,0,0,.25)}
.hero-visual{position:absolute;left:400px;top:20px;width:200px;height:190px;background:radial-gradient(circle at 50% 45%,#ffffff 0%,#e8e8e8 50%,rgba(200,60,60,.15) 70%,rgba(220,220,220,0) 80%)}
.hero-arrow{position:absolute;top:107px;width:13px;height:13px;background:#d6d6d6}
.hero-arrow svg{display:block}

/* publications */
.section-title{position:absolute;left:112px;top:336px;font-family:"Oswald",sans-serif;font-weight:400;font-size:17.5px;color:var(--red)}
.post{position:absolute;left:112px;width:530px;height:130px}
.post-image{position:absolute;left:0;top:0;width:243px;height:128px}
.post-title{position:absolute;left:259px;top:2px;font-family:"Oswald",sans-serif;font-size:9px;color:var(--red)}
.post-date{position:absolute;left:262px;top:18px;font-family:"Oswald",sans-serif;font-size:6.5px;color:#333}
.post-text{position:absolute;left:262px;width:265px;font-size:5.2px;line-height:9.6px;font-style:italic;color:var(--muted)}
.post-text.first{top:32px}
.post-text.second{top:80px}
.post-button{position:absolute;left:263px;top:110px;width:71px;height:15px;background:var(--red);border-radius:2px;color:var(--white);font-size:5px;font-weight:600;line-height:15px;text-align:center}

/* footer */
.site-footer{position:absolute;left:0;top:992px;width:750px;height:176px;background:var(--red)}
.feed-brand{position:absolute;left:112px;top:13px;font-family:"Oswald",sans-serif;font-weight:500;font-size:18px;color:var(--white);display:flex;align-items:center;gap:6px}
.feed-brand span.mark{width:10px;height:10px;border-radius:50%;background:var(--white)}
.tweet{position:absolute;left:112px;width:240px;font-size:5.6px;line-height:11px;color:var(--white)}
.tweet u{text-decoration:underline}
.follow{position:absolute;left:113px;top:147px;width:96px;height:15px;border:1px solid #7e211c;background:var(--red-deep);color:var(--white);font-size:5.5px;font-style:italic;line-height:13px;text-align:center}
.subscribe-title{position:absolute;left:380px;top:16px;font-family:"Oswald",sans-serif;font-size:15.5px;color:var(--white)}
.field{position:absolute;left:382px;width:219px;height:20px;background:var(--red-input);border:1px solid #8a241f;box-shadow:inset 0 1px 2px rgba(0,0,0,.3);font-size:6px;font-style:italic;color:#f3d6d4;line-height:18px;padding-left:9px}
.subscribe-btn{position:absolute;left:384px;top:118px;width:130px;height:26px;border-radius:2px;background:linear-gradient(#d8d8d8,#a9a9a9);border:1px solid #888;font-family:"Oswald",sans-serif;font-size:11px;color:#555;line-height:24px;text-align:center}
.bottom-bar{position:absolute;left:0;top:1168px;width:750px;height:32px;background:var(--red-dark)}
.bottom-nav{position:absolute;left:115px;top:13px;font-size:5px;color:var(--white);word-spacing:1px}
.copyright{position:absolute;left:490px;top:13px;font-size:4.8px;color:var(--white)}
</style>
</head>
<body>

<header class="site-header">
  <div class="nav-band"></div>
  <div class="brand">
    <span class="brand-name">Solène<br>Verbruggen</span>
    <span class="brand-tag">GESTION D'ENJEUX<br>AFFAIRES PUBLIQUES</span>
  </div>
  <nav class="main-nav">
    <a class="active" href="#" style="width:79px">ACCUEIL</a>
    <a href="#" style="width:58px">AGENCE</a>
    <a href="#" style="width:74px">SERVICES</a>
    <a href="#" style="width:70px">APPROCHE</a>
    <a href="#" style="width:88px">PUBLICATIONS</a>
    <a href="#" style="width:70px">CONTACT</a>
  </nav>
  <div class="social"><span></span><span></span><span></span></div>
  <div class="lang-label">Select Language :</div>
  <div class="lang-select"><i></i>English
    <svg width="6" height="4" viewBox="0 0 6 4"><path d="M0 0 L3 3 L6 0" stroke="#444" fill="none"/></svg>
  </div>
</header>

<section class="hero">
  <h1 class="hero-title">CABINET-CONSEIL EN COMMUNICATIONS<br>ET AFFAIRES PUBLIQUES SPÉCIALISÉ<br>DANS LE SECTEUR DE LA SANTÉ.</h1>
  <div class="hero-cta">EN SAVOIR PLUS</div>
  <div class="hero-visual" role="img" aria-label="Cube blanc en trois dimensions dont la face supérieure forme une croix rouge"></div>
  <div class="hero-arrow" style="left:85px"><svg width="13" height="13"><path d="M8 4 L5 6.5 L8 9" stroke="#fff" fill="none"/></svg></div>
  <div class="hero-arrow" style="left:648px"><svg width="13" height="13"><path d="M5 4 L8 6.5 L5 9" stroke="#fff" fill="none"/></svg></div>
</section>

<h2 class="section-title">PUBLICATION RÉCENTES</h2>

<article class="post" style="top:374px">
  <div class="post-image" role="img" aria-label="Mains tapant sur le clavier d'un ordinateur portable" style="background:linear-gradient(135deg,#f2ede8,#d9cfc6 55%,#a9a7a6)"></div>
  <h3 class="post-title">TITRE DE LA PUBLICATION</h3>
  <div class="post-date">23 JUILLET 2013</div>
  <p class="post-text first">Lorem ipsum dolor sit amet, consectetur adipisicing elit, sed do eiusmod tempor incididunt ut labore et dolore magna aliqua. Ut enim ad minim veniam, quis nostrud exercitation ullamco laboris nisi ut aliquip ex ea commodo consequat. Duis aute irure dolor in reprehenderit in voluptate velit esse cillum dolore eu fugiat nulla pariatur. Excepteur sint occaecat cupidatat non proident...</p>
  <p class="post-text second">Velit esse cillum dolore eu fugiat nulla pariatur. Excepteur sint occaecat cupidatat non proident, sunt in culpa qui officia deserunt mollit anim id est laborum.</p>
  <div class="post-button">ARTICLE COMPLET</div>
</article>

<article class="post" style="top:529px">
  <div class="post-image" role="img" aria-label="Homme d'affaires en costume tenant un globe terrestre" style="background:linear-gradient(90deg,#8fb3d1,#3d4a57 55%,#1d1f22)"></div>
  <h3 class="post-title">TITRE DE LA PUBLICATION</h3>
  <div class="post-date">23 JUILLET 2013</div>
  <p class="post-text first">Lorem ipsum dolor sit amet, consectetur adipisicing elit, sed do eiusmod tempor incididunt ut labore et dolore magna aliqua. Ut enim ad minim veniam, quis nostrud exercitation ullamco laboris nisi ut aliquip ex ea commodo consequat. Duis aute irure dolor in reprehenderit in voluptate velit esse cillum dolore eu fugiat nulla pariatur. Excepteur sint occaecat cupidatat non proident...</p>
  <p class="post-text second">Velit esse cillum dolore eu fugiat nulla pariatur. Excepteur sint occaecat cupidatat non proident, sunt in culpa qui officia deserunt mollit anim id est laborum.</p>
  <div class="post-button">ARTICLE COMPLET</div>
</article>

<article class="post" style="top:684px">
  <div class="post-image" role="img" aria-label="Deux collègues travaillant ensemble à un bureau" style="background:linear-gradient(135deg,#e9ecef,#c7cdd3 50%,#8c8f93)"></div>
  <h3 class="post-title">TITRE DE LA PUBLICATION</h3>
  <div class="post-date">23 JUILLET 2013</div>
  <p class="post-text first">Lorem ipsum dolor sit amet, consectetur adipisicing elit, sed do eiusmod tempor incididunt ut labore et dolore magna aliqua. Ut enim ad minim veniam, quis nostrud exercitation ullamco laboris nisi ut aliquip ex ea commodo consequat. Duis aute irure dolor in reprehenderit in voluptate velit esse cillum dolore eu fugiat nulla pariatur. Excepteur sint occaecat cupidatat non proident...</p>
  <p class="post-text second">Velit esse cillum dolore eu fugiat nulla pariatur. Excepteur sint occaecat cupidatat non proident, sunt in culpa qui officia deserunt mollit anim id est laborum.</p>
  <div class="post-button">ARTICLE COMPLET</div>
</article>

<article class="post" style="top:839px">
  <div class="post-image" role="img" aria-label="Mains tenant un stylo au-dessus d'un graphique imprimé" style="background:linear-gradient(135deg,#c9a080,#e8e4df 50%,#b9c6cf)"></div>
  <h3 class="post-title">TITRE DE LA PUBLICATION</h3>
  <div class="post-date">23 JUILLET 2013</div>
  <p class="post-text first">Lorem ipsum dolor sit amet, consectetur adipisicing elit, sed do eiusmod tempor incididunt ut labore et dolore magna aliqua. Ut enim ad minim veniam, quis nostrud exercitation ullamco laboris nisi ut aliquip ex ea commodo consequat. Duis aute irure dolor in reprehenderit in voluptate velit esse cillum dolore eu fugiat nulla pariatur. Excepteur sint occaecat cupidatat non proident...</p>
  <p class="post-text second">Velit esse cillum dolore eu fugiat nulla pariatur. Excepteur sint occaecat cupidatat non proident, sunt in culpa qui officia deserunt mollit anim id est laborum.</p>
  <div class="post-button">ARTICLE COMPLET</div>
</article>

<footer class="site-footer">
  <div class="feed-brand">Chirpline <span class="mark"></span></div>
  <p class="tweet" style="top:50px">Velit esse cillum dolore eu fugiat nulla pariatur. Excepteur sint occaecat cupidatat non proident. <u>@SoleneVerbruggen #EnjeuSanté</u></p>
  <p class="tweet" style="top:82px">Velit esse cillum dolore eu fugiat nulla pariatur. Excepteur sint occaecat cupidatat non proident. <u>@SoleneVerbruggen #EnjeuSanté</u></p>
  <p class="tweet" style="top:114px">Velit esse cillum dolore eu fugiat nulla pariatur. Excepteur sint occaecat cupidatat non proident. <u>@SoleneVerbruggen #EnjeuSanté</u></p>
  <div class="follow">Suivre @SoleneVerbruggen</div>

  <h2 class="subscribe-title">RECEVEZ NOS PUBLICATIONS</h2>
  <div class="field" style="top:51px">Votre nom</div>
  <div class="field" style="top:85px">Votre courriel</div>
  <div class="subscribe-btn">Abonnez-Vous</div>
</footer>

<div class="bottom-bar">
  <div class="bottom-nav">ACCUEIL &nbsp; | &nbsp; AGENCE &nbsp; | &nbsp; SERVICES &nbsp; | &nbsp; APPROCHE &nbsp; | &nbsp; PUBLICATIONS &nbsp; | &nbsp; CONTACT</div>
  <div class="copyright">COPYRIGHTS© 2013. SOLÈNE VERBRUGGEN. ALL RIGHTS RESERVED.</div>
</div>

</body>
</html>
```